Harlow Smokehouse World Famous BBQ Sauce Label Low And Slow Til Dusk

Looking for a eye popping BBQ sauce label. Were a family business called Harlow Smokehouse ran by 3 Big Brothers. This our first sauce were bottling its tangy sweet with a bit of spice. Our colors are yellow, black, red, gold. We either wanna go super simple or really bold. maybe even burlap as a background.

Industry/Entity Type

Business

```html
<!DOCTYPE html>
<html lang="en">
<head>
<meta charset="utf-8">
<title>Harlow Smokehouse – Famous Original BBQ Sauce Label</title>
<link rel="stylesheet" href="https://fonts.googleapis.com/css2?family=Teko:wght@500;600&display=swap">
<style>
  :root {
    --canvas: #ffffff;
    --gold-top: #c7b13a;
    --yellow-mid: #e0da49;
    --ember-red: #c4301a;
    --ember-deep: #7d1412;
    --ember-glow: #ef7a3a;
    --badge-black: #0e0c0a;
    --badge-edge: #c9a227;
    --type-yellow: #f4e21c;
    --type-outline: #1a1208;
    --brand-red: #c0290f;
    --tagline-white: #ffffff;
  }
  * { box-sizing: border-box; margin: 0; padding: 0; }
  html, body { width: 1200px; height: 1000px; overflow: hidden; background: var(--canvas); }
  .canvas { position: relative; width: 1200px; height: 1000px; }

  .label {
    position: absolute; left: 412px; top: 166px; width: 375px; height: 665px;
    overflow: hidden;
    background: linear-gradient(180deg, var(--gold-top) 0%, var(--yellow-mid) 38%, var(--yellow-mid) 45%, var(--ember-glow) 62%);
    font-family: "Teko", "Arial Narrow", sans-serif;
  }
  .label__embers {
    position: absolute; left: 0; right: 0; top: 300px; bottom: 0;
    background:
      radial-gradient(ellipse 60% 30% at 30% 45%, rgba(255,190,140,.55), transparent 70%),
      radial-gradient(ellipse 50% 25% at 75% 60%, rgba(255,160,110,.45), transparent 70%),
      linear-gradient(180deg, rgba(224,218,73,0) 0%, var(--ember-glow) 18%, var(--ember-red) 45%, var(--ember-deep) 100%);
  }
  .badge { position: absolute; left: 25px; top: 14px; width: 325px; height: 178px; }
  .badge__art {
    position: absolute; left: 38px; top: 22px; width: 250px; height: 150px;
    border-radius: 40px 40px 0 0;
    background: radial-gradient(ellipse 50% 60% at 50% 55%, #e8a531 0%, #6b3a18 55%, #1a1410 100%);
  }
  .brand {
    position: absolute; left: 0; right: 0; top: 183px;
    text-align: center; color: var(--brand-red);
    font-weight: 600; font-size: 54px; line-height: 46px; letter-spacing: 1px;
    text-transform: uppercase;
  }
  .product { position: absolute; left: 0; right: 0; text-align: center; color: var(--type-yellow); font-weight: 500;
    text-shadow: -2px -2px 0 var(--type-outline), 2px -2px 0 var(--type-outline), -2px 2px 0 var(--type-outline), 2px 2px 0 var(--type-outline); }
  .product--kicker { top: 336px; font-size: 50px; line-height: 50px; }
  .product--name { top: 392px; font-size: 96px; line-height: 90px; letter-spacing: 1px; }
  .tagline {
    position: absolute; left: 0; right: 0; top: 578px; text-align: center;
    color: var(--tagline-white); font-weight: 500; font-size: 38px; line-height: 40px;
    text-transform: uppercase; letter-spacing: 1px;
  }
</style>
</head>
<body>
<main class="canvas">
  <section class="label" aria-label="BBQ sauce label">
    <div class="label__embers" role="img" aria-label="Glowing red embers with drifting smoke"></div>

    <svg class="badge" viewBox="0 0 325 178" aria-hidden="true">
      <path d="M30 178 C30 140 10 120 8 95 C6 70 30 48 38 38 C70 30 90 14 120 10 C150 4 175 4 205 10 C235 14 255 30 287 38 C295 48 319 70 317 95 C315 120 295 140 295 178 Z"
            fill="var(--badge-black)" stroke="var(--badge-edge)" stroke-width="2"/>
    </svg>
    <div class="badge__art" style="left:63px;top:36px;" role="img" aria-label="Illustration of three brothers standing with arms crossed"></div>

    <h1 class="brand">Harlow<br>Smokehouse</h1>

    <p class="product product--kicker">Famous Original</p>
    <p class="product product--name">BBQ SAUCE</p>

    <p class="tagline">Low And Slow Til Dusk</p>
  </section>
</main>
</body>
</html>
```